Vordaline - Fitness Coach. Needs a Business Card Design that I can also use for other advertising

Established 2012, I have finished the KTRB National Certificate in Fitness & Personal Training. Harlow Cross First Aid Certificate. I have the Auckland 800m track records for MW45. I also came 1st at the 2012 Pellamar Games in 800 & 1500m. I am passionate about health & fitness and would like to help people reach their health & fitness goals. I also take health & fitness weekends. Main interests - Running, Weight Training, Yoga & Aqua Jogging. I like strength/power, but am femine.

Target Market(s)

Male or Female 18 and over that wants to improve their health & fitness

Industry/Entity Type

Advertising

Requirements
Must have
• my name: Rosalind K Tarbury contact details: ros@quillsend.co.nz mobile - 021 583917 URL name: facebook.com/rosalindKtarbury - VordaLine
Photo of Me

```html
<!DOCTYPE html>
<html lang="en">
<head>
<meta charset="utf-8">
<title>VordaLine Fitness Coach – Business Card</title>
<link rel="stylesheet" href="https://fonts.googleapis.com/css2?family=PT+Sans:ital,wght@0,400;0,700;1,700&display=swap">
<style>
  :root {
    --page-bg: #eeeeee;
    --card-bg: #ffffff;
    --brand-green: #0c4a2a;
    --accent-green: #2a9a48;
    --magenta: #c2337f;
    --photo-dark: #1f3d1c;
    --photo-mid: #3f6b2c;
    --photo-grass: #6fa23a;
  }
  * { margin: 0; padding: 0; box-sizing: border-box; }
  html, body {
    width: 1200px; height: 965px; overflow: hidden;
    background: var(--page-bg);
    font-family: "PT Sans", sans-serif;
  }
  .business-card {
    position: absolute; left: 50px; top: 166px;
    width: 1100px; height: 632px;
    background: var(--card-bg);
    box-shadow: 0 3px 10px rgba(0,0,0,0.25);
  }
  .coach-photo {
    position: absolute; left: 0; top: 0;
    width: 485px; height: 632px;
    background: linear-gradient(180deg, var(--photo-dark) 0%, var(--photo-mid) 70%, var(--photo-grass) 100%);
  }
  .divider-bar {
    position: absolute; left: 485px; top: 0;
    width: 13px; height: 632px;
    background: var(--magenta);
  }
  .divider-arrow {
    position: absolute; left: 497px; top: 366px;
  }
  .brand-block {
    position: absolute; left: 583px; top: 84px;
    width: 420px; text-align: right;
  }
  .brand-name {
    font-size: 84px; font-weight: 700; line-height: 1;
    color: var(--brand-green); text-align: left;
  }
  .brand-tagline {
    font-size: 30px; font-weight: 400; line-height: 1;
    color: var(--accent-green); margin-top: 6px;
  }
  .coach-name {
    position: absolute; left: 585px; top: 374px;
    font-size: 40px; font-weight: 700; font-style: italic;
    color: var(--magenta);
  }
  .contact-list {
    position: absolute; left: 588px; top: 434px;
    list-style: none;
  }
  .contact-item {
    display: flex; align-items: center;
    height: 41px;
    font-size: 31px; color: var(--brand-green);
  }
  .contact-icon { width: 28px; height: 30px; margin-right: 16px; flex: none; }
</style>
</head>
<body>
  <div class="business-card">
    <div class="coach-photo" role="img" aria-label="Photo of the fitness coach jumping in the air in front of a green hedge on a lawn"></div>
    <div class="divider-bar"></div>
    <svg class="divider-arrow" width="34" height="62" viewBox="0 0 34 62">
      <polygon points="0,0 34,31 0,62" fill="var(--magenta)"/>
    </svg>

    <div class="brand-block">
      <div class="brand-name">VordaLine</div>
      <div class="brand-tagline">Fitness Coach</div>
    </div>

    <div class="coach-name">Rosalind K Tarbury</div>

    <ul class="contact-list">
      <li class="contact-item">
        <svg class="contact-icon" viewBox="0 0 28 30" aria-hidden="true">
          <rect x="6" y="1" width="16" height="28" rx="3" fill="none" stroke="var(--magenta)" stroke-width="3"/>
          <rect x="11" y="24" width="6" height="2" fill="var(--magenta)"/>
        </svg>
        021 583917
      </li>
      <li class="contact-item">
        <svg class="contact-icon" viewBox="0 0 28 30" aria-hidden="true">
          <rect x="1" y="7" width="26" height="17" fill="var(--magenta)"/>
          <polyline points="1,7 14,17 27,7" fill="none" stroke="#fff" stroke-width="2"/>
          <line x1="1" y1="24" x2="11" y2="15" stroke="#fff" stroke-width="2"/>
          <line x1="27" y1="24" x2="17" y2="15" stroke="#fff" stroke-width="2"/>
        </svg>
        ros@quillsend.co.nz
      </li>
      <li class="contact-item">
        <svg class="contact-icon" viewBox="0 0 28 30" aria-hidden="true">
          <rect x="3" y="6" width="22" height="22" fill="var(--magenta)"/>
        </svg>
        rosalindKtarbury
      </li>
    </ul>
  </div>
</body>
</html>
```